Club sale for moms — 3 static banners

Lullavo is the largest daily deal site for moms, kids and babies in Russia, which provides offers with discounts up to 70%.
We need 3 banners for our flash sale, all banners must be on a white background, all must be static and be in 2 versions, so when you hover over banner the picture changes. Banners' style should differ from other banners which refer to deals (like pebbloo's banners "Invite a friend, earn $20", they are attached).
Purpose: filling the empty space on the main page in case of absence of the necessary number of deals' banners. The example of our main page is attached.
1st static banner:
474px × 308px
text: Пригласите друга — получите бонус на следующую покупку!
That text means: Invite a friend and get a bonus for shopping.
After clicking on that banner a client will go to the site section "Invites".
The text means: Invite a friend and get a bonus for shopping.
2nd static banner:
308px × 199px
Text: Доставка по всей России. Оплата при получении.
After clicking on that banner a client will go to the site section about delivery.
The text means: Delivery all over Russia, pay on getting.
3rd static banner:
308px × 199px
Text:
Гарантия лучшей цены!
The text means:
Best price guarantee
Target Market(s)
moms
Industry/Entity Type
Club
Look and feel
Each slider illustrates characteristics of the customer's brand and the style your logo design should communicate.

```html
<!DOCTYPE html>
<html lang="ru">
<head>
<meta charset="utf-8">
<title>Пригласите друга — баннеры</title>
<link rel="stylesheet" href="https://fonts.googleapis.com/css2?family=PT+Sans:wght@400&display=swap">
<style>
  :root {
    --stage-bg: #52565a;
    --banner-bg: #ffffff;
    --title-red: #d0121b;
    --title-pink: #c8286e;
    --lead-blue: #2c5d8f;
    --lead-gray: #7b7b7b;
    --photo-red-top: #eef1f5;
    --photo-red-mid: #c7413f;
    --photo-red-low: #4e6f97;
    --photo-blue-top: #f1f1f1;
    --photo-blue-mid: #6f8aa5;
    --photo-blue-low: #3f6387;
  }
  * { box-sizing: border-box; margin: 0; padding: 0; }
  html, body {
    width: 1200px;
    height: 900px;
    overflow: hidden;
    background: var(--stage-bg);
    font-family: "PT Sans", "Myriad Pro", Arial, sans-serif;
  }
  .stage {
    position: relative;
    width: 1200px;
    height: 900px;
  }
  .banner {
    position: absolute;
    top: 162px;
    width: 470px;
    height: 570px;
    background: var(--banner-bg);
    overflow: hidden;
  }
  .banner--red { left: 120px; }
  .banner--pink { left: 606px; }
  .banner__title {
    position: absolute;
    left: 31px;
    top: 26px;
    font-size: 50px;
    font-weight: 400;
    line-height: 1.1;
    letter-spacing: -0.3px;
    white-space: nowrap;
    z-index: 2;
  }
  .banner--red .banner__title { color: var(--title-red); }
  .banner--pink .banner__title { color: var(--title-pink); }
  .banner__lead {
    position: absolute;
    left: 31px;
    top: 86px;
    font-size: 30px;
    line-height: 41.5px;
    white-space: nowrap;
    z-index: 2;
  }
  .banner--red .banner__lead { color: var(--lead-blue); }
  .banner--pink .banner__lead { color: var(--lead-gray); }
  .banner__photo {
    position: absolute;
    opacity: 0.85;
  }
  .banner--red .banner__photo {
    left: 186px;
    top: 126px;
    width: 246px;
    height: 426px;
    background: linear-gradient(180deg, var(--photo-red-top) 0%, var(--photo-red-mid) 35%, var(--photo-red-low) 75%, var(--photo-red-top) 100%);
    clip-path: polygon(52px 0, 100% 0, 100% 100%, 0 100%, 0 96px, 52px 96px);
  }
  .banner--pink .banner__photo {
    left: 174px;
    top: 168px;
    width: 296px;
    height: 402px;
    background: linear-gradient(180deg, var(--photo-blue-top) 0%, var(--photo-blue-mid) 30%, var(--photo-blue-low) 100%);
    clip-path: polygon(62px 0, 100% 0, 100% 100%, 0 100%, 0 48px, 62px 48px);
  }
</style>
</head>
<body>
  <main class="stage">
    <section class="banner banner--red">
      <h1 class="banner__title">Пригласите друга</h1>
      <p class="banner__lead">получите бонус<br>на следующую<br>покупку!</p>
      <div class="banner__photo" role="img" aria-label="Фото: два улыбающихся мальчика стоят в обнимку, один в синей кофте, другой в красной"></div>
    </section>
    <section class="banner banner--pink">
      <h1 class="banner__title">Пригласите друга</h1>
      <p class="banner__lead">получите бонус<br>на следующую<br>покупку!</p>
      <div class="banner__photo" role="img" aria-label="Фото: два смеющихся мальчика в джинсах сидят обнявшись"></div>
    </section>
  </main>
</body>
</html>
```